Design a cover for a new book!

Design a cover for a new book called "Where Rivers Forget Their Stones" Subtitle is "Seven Lanterns Beneath One Painted Northern Harbor Sky"

The brief attached will give you the theme of the book. The book tells how there are two economies, one controlled by people who own financial assets, and the other run by people who build real things that contribute to our standard of living.

We want a split cover showing two different economies existing at the same time. The cover should show a split scene! Half the cover should be the monetary economy - the stock market or derivative or commodities. The other half the cover should show the material economy - technology and manufacturing, or maybe people living and doing things.

Target Market(s)

General Audience, people who like political policy

Industry/Entity Type

economics

Requirements
Must have
• The cover should show a split scene! Half the cover should be the monetary economy - the stock market or derivative or commodities. The other half the cover should show the material economy - technology and manufacturing,

```html
<!DOCTYPE html>
<html lang="en">
<head>
<meta charset="utf-8">
<title>Where Rivers Forget Their Stones — Cover Wrap</title>
<link href="https://fonts.googleapis.com/css2?family=Lato:wght@300;400;700;900&display=swap" rel="stylesheet">
<style>
  :root {
    --crimson: #bd1541;
    --crimson-text: #b3163f;
    --paper: #ffffff;
    --ink-light: #ffffff;
    --spine-ink: #b3163f;
    --barcode-box: #d9d9d9;
    --market-deep: #1b2a6b;
    --market-mid: #4660b8;
    --market-glow: #7fb7ff;
    --factory-dark: #1c2430;
    --factory-mid: #3a4656;
    --factory-yellow: #e3a51c;
  }
  * { margin: 0; padding: 0; box-sizing: border-box; }
  html, body { width: 1200px; height: 914px; overflow: hidden; background: var(--paper); }
  .cover-wrap {
    position: relative; width: 1200px; height: 914px; overflow: hidden;
    background: var(--paper); font-family: "Lato", Arial, sans-serif;
  }

  /* ---------- Back cover ---------- */
  .back-headline {
    position: absolute; left: 54px; top: 57px; width: 500px;
    text-align: center; font-weight: 700; font-size: 18.5px; color: var(--crimson-text);
  }
  .back-blurb {
    position: absolute; left: 54px; top: 106px; width: 500px;
    font-weight: 300; font-size: 15.6px; line-height: 21px; color: var(--crimson-text);
    text-align: justify;
  }
  .back-blurb strong { font-weight: 700; }
  .back-band {
    position: absolute; left: 0; top: 300px; width: 590px; height: 310px;
    background: var(--crimson);
    clip-path: polygon(0 10px, 40px 4px, 70px 9px, 110px 2px, 150px 8px, 190px 3px, 240px 10px, 280px 5px, 330px 9px, 370px 2px, 420px 8px, 460px 4px, 510px 10px, 550px 3px, 590px 8px,
      590px 300px, 550px 306px, 500px 298px, 460px 305px, 410px 300px, 360px 308px, 310px 299px, 260px 305px, 210px 297px, 160px 306px, 110px 300px, 60px 307px, 0 299px);
  }
  .endorsement {
    position: absolute; left: 54px; top: 50px; width: 500px;
    font-size: 16px; line-height: 21.2px; color: var(--ink-light); text-align: justify;
  }
  .endorsement-source {
    position: absolute; right: 36px; top: 258px;
    font-size: 16px; color: var(--ink-light);
  }
  .author-photo {
    position: absolute; left: 22px; top: 622px; width: 113px; height: 132px;
    background: linear-gradient(160deg, #5a6b4a 0%, #8a6a50 45%, #b3283a 80%, #2a2a2a 100%);
  }
  .author-bio {
    position: absolute; left: 146px; top: 636px; width: 401px;
    font-weight: 300; font-size: 15.6px; line-height: 20px; color: var(--crimson-text);
    text-align: justify;
  }
  .barcode-box {
    position: absolute; left: 353px; top: 749px; width: 207px; height: 124px;
    background: var(--barcode-box);
  }

  /* ---------- Spine ---------- */
  .spine-title, .spine-author {
    position: absolute; left: 599px; writing-mode: vertical-rl;
    color: var(--spine-ink); text-transform: uppercase; white-space: nowrap;
  }
  .spine-title { top: 322px; font-size: 11.5px; letter-spacing: 2.2px; font-weight: 400; }
  .spine-author { top: 690px; font-size: 10.5px; letter-spacing: 1.8px; font-weight: 400; }

  /* ---------- Front cover ---------- */
  .market-scene {
    position: absolute; left: 612px; top: 0; width: 588px; height: 320px;
    background:
      linear-gradient(90deg, transparent 0%, transparent 40%, rgba(127,183,255,0.35) 70%, rgba(200,60,160,0.35) 100%),
      linear-gradient(135deg, #9fb0e0 0%, var(--market-mid) 40%, var(--market-deep) 100%);
  }
  .market-bars { position: absolute; left: 0; top: 0; }
  .factory-scene {
    position: absolute; left: 612px; top: 610px; width: 588px; height: 304px;
    background:
      radial-gradient(ellipse at 60% 10%, rgba(255,200,120,0.45), transparent 55%),
      linear-gradient(90deg, var(--factory-mid) 0%, var(--factory-dark) 40%, #4a4030 70%, var(--factory-yellow) 100%);
  }
  .front-tear {
    position: absolute; left: 612px; top: 292px; width: 588px; height: 344px;
    background: var(--paper);
    clip-path: polygon(0 8px, 45px 2px, 90px 9px, 130px 0, 180px 7px, 220px 2px, 270px 10px, 320px 3px, 360px 8px, 410px 1px, 450px 9px, 500px 3px, 545px 8px, 588px 2px,
      588px 336px, 540px 344px, 495px 334px, 450px 342px, 400px 335px, 350px 343px, 300px 333px, 250px 341px, 200px 334px, 150px 343px, 100px 335px, 50px 342px, 0 334px);
  }
  .front-band {
    position: absolute; left: 612px; top: 296px; width: 588px; height: 336px;
    background: var(--crimson);
    clip-path: polygon(0 10px, 45px 5px, 90px 11px, 130px 3px, 180px 9px, 220px 5px, 270px 12px, 320px 6px, 360px 10px, 410px 4px, 450px 11px, 500px 6px, 545px 10px, 588px 5px,
      588px 328px, 540px 335px, 495px 326px, 450px 333px, 400px 327px, 350px 334px, 300px 325px, 250px 332px, 200px 326px, 150px 334px, 100px 327px, 50px 333px, 0 326px);
  }
  .book-title {
    position: absolute; left: 0; top: 68px; width: 100%;
    text-align: center; color: var(--ink-light);
    font-weight: 400; font-size: 45px; line-height: 56px; text-transform: uppercase;
  }
  .book-title .line-strong { font-weight: 700; }
  .book-subtitle {
    position: absolute; left: 0; top: 198px; width: 100%;
    text-align: center; color: var(--ink-light);
    font-weight: 700; font-size: 22.5px; line-height: 31px;
    text-shadow: 0 1px 2px rgba(0,0,0,0.35);
  }
  .book-author {
    position: absolute; left: 0; top: 268px; width: 100%;
    text-align: center; color: var(--ink-light);
    font-weight: 700; font-size: 31px; letter-spacing: 0.5px; text-transform: uppercase;
  }
</style>
</head>
<body>
<main class="cover-wrap">

  <!-- Back cover -->
  <section class="back-cover">
    <h2 class="back-headline">It is the best of times, it is the worst of times.</h2>
    <p class="back-blurb"><strong>Where Rivers Forget Their Stones</strong> details the battle between the material and monetary economies. While the development of modern technology in our material economy has us on the brink of prosperity, a turf war in our monetary economy is destroying our prospects for enjoying this success. This book provides solutions to reverse the erosion of our standard of living caused by our monetary economy with an upgrade to our financial operating system that would benefit both rich and poor.</p>

    <div class="back-band">
      <blockquote class="endorsement">“Whether you are a political pundit, economist, or Wall Street banker, Where Rivers Forget Their Stones is a must-read on what ails our nation today. This book sets the story straight on a battle between two economies and offers a stunning way out of our financial travails. The solution’s brilliance is in its simplicity. In one fell swoop, author Daniel Marlow wipes out income taxes, balances the budget, and sets our nation on a path to paying off its national debt, while also affording new benefits that would catapult our nation into an era of unprecedented prosperity.”</blockquote>
      <p class="endorsement-source">—Gregory Halvorsen</p>
    </div>

    <div class="author-photo" role="img" aria-label="Portrait photograph of the author outdoors"></div>
    <p class="author-bio">Daniel Marlow is an early pioneer of structured finance and a serial entrepreneur, having co-founded software technology companies, charter schools, and an international publication for students. He enjoys painting galaxies and writing about the economy.</p>
    <div class="barcode-box"></div>
  </section>

  <!-- Spine -->
  <section class="spine">
    <p class="spine-title">Where Rivers Forget Their Stones</p>
    <p class="spine-author">Daniel Reeve Marlow</p>
  </section>

  <!-- Front cover -->
  <section class="front-cover">
    <div class="market-scene" role="img" aria-label="Banknote engraving overlaid with glowing stock market candlestick charts and price figures">
      <svg class="market-bars" width="588" height="320" viewBox="0 0 588 320" aria-hidden="true">
        <g fill="#7fd0ff" opacity="0.55">
          <rect x="250" y="120" width="6" height="110"/>
          <rect x="272" y="90" width="6" height="130"/>
          <rect x="296" y="60" width="7" height="120"/>
          <rect x="320" y="40" width="6" height="100"/>
          <rect x="345" y="20" width="7" height="130"/>
          <rect x="370" y="10" width="6" height="80"/>
          <rect x="395" y="0" width="7" height="110"/>
          <rect x="420" y="15" width="6" height="70"/>
        </g>
        <g fill="#ff5aa8" opacity="0.45">
          <rect x="470" y="40" width="6" height="90"/>
          <rect x="500" y="70" width="6" height="80"/>
          <rect x="530" y="30" width="6" height="120"/>
          <rect x="560" y="60" width="6" height="90"/>
        </g>
      </svg>
    </div>
    <div class="factory-scene" role="img" aria-label="Engineer in a hard hat holding a laptop beside yellow robotic arms on a factory line"></div>

    <div class="front-tear"></div>
    <div class="front-band">
      <h1 class="book-title">Where Rivers<br><span class="line-strong">Forget Their Stones</span></h1>
      <p class="book-subtitle">Seven Lanterns Beneath One Painted<br>Northern Harbor Sky</p>
      <p class="book-author">Daniel Reeve Marlow</p>
    </div>
  </section>

</main>
</body>
</html>
```